Math Help Website Needs New Design

Looking to refresh the design of my existing site (quillnumberdesk.com) to be easier on the eyes. I am fully capable of doing the HTML coding and have for years, but I don't have the eye for good design, colors, layout, and fonts. This is where I need help!

I need both a new design scheme and a new logo that matches. The overall functionality will be the same as the existing site, and should not be unrecognizable.

Target Market(s)

It should appeal to students (age 13-22) and their parents, so it should NOT be childish in appearance, nor should it be corporate.

Requirements
Must have
• Should be simple, easy-to-navigate, and neither childish nor corporate. I am looking for a design for both the homepage and a similar "content" page. Simple, bold colors are preferred. A logo should be prominent at the top, with a search bar nearby. Below that I need a similar navigational area like I already have. Then, I need about 200px wide ad space on the left of the main body area.

```html
<!DOCTYPE html>
<html lang="en">
<head>
<meta charset="utf-8">
<title>Quill Number Desk</title>
<link href="https://fonts.googleapis.com/css2?family=PT+Sans:wght@400;700&family=Arimo:ital,wght@0,400;0,700;1,400&display=swap" rel="stylesheet">
<style>
:root{
  --sky:#8ecadf;
  --paper:#ffffff;
  --panel:#f7f7f7;
  --line:#e2e2e2;
  --ink:#222;
  --muted:#555;
  --teal:#7fc3d6;
  --link:#3a93c2;
  --nav:#3d3d3d;
  --green:#5a9a1a;
  --red:#d7191c;
  --btn:#9fd4e3;
}
*{box-sizing:border-box;margin:0;padding:0}
html,body{width:900px;height:1200px;overflow:hidden}
body{background:var(--sky);font-family:"Arimo",Arial,sans-serif;color:var(--ink);position:relative}
.abs{position:absolute}
.page{left:88px;top:15px;width:724px;height:1112px;background:var(--paper);border-radius:10px 10px 0 0}
.brand{left:104px;top:46px;display:flex;align-items:center;gap:8px;font-family:"PT Sans",sans-serif;font-weight:700;font-size:24px;color:#2b6fb6}
.brand-dot{width:16px;height:16px;border-radius:50%;background:#e8473c}
.search{left:572px;top:44px;width:205px;height:30px;border:1px solid #ddd;border-radius:6px;background:#f6f6f6}
.search svg{position:absolute;right:8px;top:6px}
.nav{left:79px;top:99px;width:741px;height:31px;background:var(--nav);display:flex;align-items:center;padding-left:6px}
.nav a{color:#fff;text-decoration:none;font-family:"PT Sans",sans-serif;font-size:12px;padding:0 18px;border-right:1px solid #666;line-height:18px}
.nav a:last-child{border:none}
.box{background:var(--panel);border:1px solid var(--line);border-radius:6px}
.ph{display:block}
.ad1-text{left:108px;top:270px;width:134px;height:56px;background:#e4e4e4;text-align:center;font-size:12px;line-height:14px;padding-top:5px}
.ad1-text b{display:block;color:#7ab23c;font-style:italic;font-size:16px;line-height:18px;font-family:"PT Sans",sans-serif}
.ad2{left:114px;top:346px;width:120px;height:271px;border:1px solid #222;background:#fff;text-align:center}
.ad2 .band{background:var(--red);color:#fff;font-family:"PT Sans",sans-serif;font-weight:700;font-size:13px;height:28px;line-height:28px}
.ad2 .words{font-family:"PT Sans",sans-serif;font-size:15px;line-height:22px;margin-top:8px}
.ad2 .view{display:inline-block;background:var(--red);color:#fff;font-size:11px;padding:1px 12px;margin-top:12px}
.ad2 .foot{position:absolute;bottom:0;left:0;right:0;height:19px;background:#111;color:#f2b705;font-size:12px;line-height:19px;font-weight:700}
h1.welcome{left:275px;top:150px;font-family:"PT Sans",sans-serif;font-size:28px;font-weight:700;color:#2c2c2c}
h1.welcome span{color:var(--teal)}
.intro{left:279px;top:197px;width:312px;font-size:10.5px;line-height:12.8px;color:#333}
.intro p+p{margin-top:12px}
.h2{font-family:"PT Sans",sans-serif;font-size:15px;font-weight:700;color:#333;letter-spacing:.3px}
.list{list-style:none}
.list li{position:relative;padding-left:14px;font-size:11px;color:#222}
.list li::before{content:"";position:absolute;left:0;top:3px;width:8px;height:8px;border-radius:50%;background:var(--link)}
.disc li{height:33.5px}
.disc i{display:block;font-size:9px;color:var(--link);margin-left:81px;margin-top:1px}
.news li{height:19.5px}
.online{left:108px;top:668px;font-size:10px;font-weight:700;color:var(--green)}
.online-sub{left:108px;top:683px;font-size:9.5px;color:#333}
.live{left:110px;top:699px;width:124px;height:42px;background:#5bb030;border-radius:3px;color:#fff;font-family:"PT Sans",sans-serif;font-size:12px;letter-spacing:2px;line-height:14px;padding:7px 0 0 48px}
.live svg{position:absolute;left:9px;top:9px}
.study-h{left:110px;top:750px;font-family:"PT Sans",sans-serif;font-size:11px;color:#444}
.study{left:110px;top:773px;width:132px;list-style:none}
.study li{display:flex;gap:6px;font-size:8px;line-height:9px;color:#888;margin-bottom:8px}
.study .av{flex:none;width:19px;height:19px;background:#bbb}
.study span b{color:var(--link);font-weight:400}
.by{left:178px;top:1062px;font-size:8px;font-weight:700;text-decoration:underline;color:#333}
.tabs{left:270px;top:655px;display:flex;font-size:10.5px}
.tabs span{padding:4px 0;margin-right:25px;height:23px}
.tabs .on{background:var(--panel);border:1px solid var(--line);border-bottom:none;border-radius:5px 5px 0 0;padding:4px 6px;font-weight:700;margin-left:-6px;margin-right:19px}
.keys{left:281px;top:690px;display:grid;grid-template-columns:repeat(10,47px);row-gap:6px;font-family:"PT Sans",sans-serif;font-size:13px;text-align:center}
.keys svg{display:block;margin:0 auto}
.lbl{font-size:10px;font-weight:700;color:#333;text-align:right;width:80px}
.field{background:#fff;border:1px solid var(--line);border-radius:6px}
.examples{font-size:10px;line-height:16.5px;padding:5px 9px}
.scroll{right:4px;top:8px;width:9px;height:94px;border:1px solid #ddd;background:#f3f3f3}
.btn{background:var(--btn);border:1px solid #6fb2c7;border-radius:6px;font-family:"PT Sans",sans-serif;font-weight:700;color:#223;text-align:center}
.footer{left:0;top:1127px;width:900px;height:73px;background:#3d3d3d;color:#fff;text-align:center;font-size:9.5px}
.footer nav{margin-top:32px}
.footer nav a{color:#fff;text-decoration:none;padding:0 6px}
.footer p{margin-top:5px}
</style>
</head>
<body>
<div class="abs page"></div>

<header>
  <div class="abs brand"><span class="brand-dot"></span>QuillNumberDesk</div>
  <div class="abs search">
    <svg width="18" height="18" viewBox="0 0 18 18"><circle cx="7" cy="7" r="5.5" fill="none" stroke="#111" stroke-width="2"/><line x1="11" y1="11" x2="16.5" y2="16.5" stroke="#111" stroke-width="2.5"/></svg>
  </div>
  <nav class="abs nav">
    <a>Home</a><a>Algebra</a><a>Geometry</a><a>Trig</a><a>Calculus</a><a>Statistics</a><a>More</a><a>Subjects</a><a>Message Board</a>
  </nav>
</header>

<aside>
  <div class="abs box" style="left:100px;top:142px;width:150px;height:491px"></div>
  <div class="abs ph" role="img" aria-label="Photo of a group of smiling students" style="left:108px;top:148px;width:134px;height:122px;background:linear-gradient(160deg,#cfe4f1,#c8773f 60%,#5c4a3e)"></div>
  <div class="abs ad1-text"><b>TEST NOW</b>Before the<br>Exam Changes!</div>
  <div class="abs ad2">
    <div role="img" aria-label="Photo of two students with books" style="height:109px;background:linear-gradient(160deg,#f1f1f1,#c9a48a 55%,#b0282a)"></div>
    <div class="band">Classes 4th - 12th</div>
    <div class="words">Worksheets<br>&amp;<br>Exercises</div>
    <span class="view">View</span>
    <div class="foot">brightpath</div>
  </div>

  <div class="abs box" style="left:100px;top:658px;width:150px;height:427px"></div>
  <div class="abs online">116 people online</div>
  <div class="abs online-sub">They can help you right now!</div>
  <div class="abs live">
    <svg width="32" height="24" viewBox="0 0 32 24"><rect x="1" y="1" width="26" height="16" rx="4" fill="#fff"/><path d="M7 17l-2 6 8-6z" fill="#fff"/></svg>
    Live Help<br>ONLINE
  </div>
  <div class="abs study-h">Live Study Group</div>
  <ul class="abs study">
    <li><span class="av"></span><span><b>x squared - y =9 define a function of x?</b> 0 replies</span></li>
    <li><span class="av"></span><span><b>What is the product of (4+3i)(5-2i)?</b> 5 replies</span></li>
    <li><span class="av"></span><span><b>Identify the hypothesis of the following statement: The rugs will be damaged if the water line breaks. ...</b> 1 reply</span></li>
    <li><span class="av"></span><span><b>Find second and third derivative of \[e^{2x^{2}}\]</b> 2 replies</span></li>
    <li><span class="av"></span><span><b>Simplify: 1-(1/a) / (1/a^2)-(1/a) ...</b> 0 replies</span></li>
    <li><span class="av"></span><span><b>Write as a single logarithm 3loga x + 4loga y- 1/3loga z</b> 3 replies</span></li>
    <li><span class="av"></span><span><b>x squared - y =9 define a function of x?</b> 0 replies</span></li>
  </ul>
  <div class="abs by">by PeerCircle</div>
</aside>

<main>
  <div class="abs box" style="left:267px;top:142px;width:531px;height:491px"></div>
  <h1 class="abs welcome">Welcome to <span>Quill Number Desk!</span></h1>
  <div class="abs intro">
    <p>Math Lessons - Looking to understand a subject better, or maybe you don't understand what your textbook is trying to tell you? We have a collection of algebra and geometry lessons that you can view online right now.</p>
    <p>Ask your question on our math help message board. Just be sure to explain what you've tried to do and where you're stuck, and a friendly volunteer may try to assist you!</p>
  </div>
  <div class="abs" role="img" aria-label="Photo of a student studying in front of a chalkboard with formulas" style="left:583px;top:180px;width:188px;height:128px;background:linear-gradient(90deg,#fff 10%,#e9e2d6 40%,#3a3a3a 55%,#2d2d2d 90%,#c49a5a)"></div>
  <div class="abs" style="left:276px;top:318px;width:514px;border-top:1px dotted #ccc"></div>

  <div class="abs h2" style="left:276px;top:322px">Current Discussions:</div>
  <ul class="abs list disc" style="left:276px;top:351px;width:240px">
    <li>Find rotation in rev/min given angula...<i>Posted by: marlowe22</i></li>
    <li>Algebraic relationship<i>Posted by: Tobias</i></li>
    <li>Graphing the movement of the Harwick ...<i>Posted by: kRenn4</i></li>
    <li>Find rotation in rev/min given angula...<i>Posted by: marlowe22</i></li>
    <li>Find rotation in rev/min given angula...<i>Posted by: marlowe22</i></li>
    <li>Find rotation in rev/min given angula...<i>Posted by: marlowe22</i></li>
    <li>Find rotation in rev/min given angula...<i>Posted by: marlowe22</i></li>
    <li>Find rotation in rev/min given angula...<i>Posted by: marlowe22</i></li>
  </ul>

  <div class="abs h2" style="left:573px;top:325px">What's New?</div>
  <ul class="abs list news" style="left:570px;top:351px;width:220px">
    <li>Multiplying Polynomials</li>
    <li>Derivative of an Inverse Function</li>
    <li>Derivatives of Logs and Exps</li>
    <li>Differentiating Trig Functions</li>
  </ul>
  <div class="abs h2" style="left:573px;top:438px">Math Lessons</div>
  <ul class="abs list news" style="left:572px;top:464px;width:200px">
    <li>Algebra</li><li>Geometry</li><li>Trigonometry</li><li>Calculus</li><li>Statistics</li><li>Sports Math</li><li>Math Games</li><li>Calculators</li>
  </ul>

  <div class="abs box" style="left:267px;top:677px;width:531px;height:421px"></div>
  <div class="abs tabs">
    <span>Basic Math</span><span>Pre-Algebra</span><span class="on">Algebra</span><span>Trigonometry</span><span>Precalculus</span><span>Calculus</span><span>Statistics</span>
  </div>
  <div class="abs keys">
    <svg width="18" height="14"><rect x="3" y="3" width="12" height="8" fill="#9fd4e3" stroke="#3a93c2"/></svg>
    <svg width="18" height="14"><rect x="3" y="3" width="12" height="8" fill="#9fd4e3" stroke="#3a93c2"/></svg>
    <svg width="18" height="14"><rect x="3" y="3" width="12" height="8" fill="#9fd4e3" stroke="#3a93c2"/></svg>
    <svg width="18" height="18"><rect x="3" y="1" width="12" height="6" fill="#9fd4e3" stroke="#3a93c2"/><line x1="1" y1="9" x2="17" y2="9" stroke="#333"/><rect x="3" y="11" width="12" height="6" fill="#9fd4e3" stroke="#3a93c2"/></svg>
    <svg width="18" height="16"><rect x="2" y="5" width="10" height="10" fill="#9fd4e3" stroke="#3a93c2"/><rect x="13" y="1" width="4" height="4" fill="#9fd4e3" stroke="#3a93c2"/></svg>
    <svg width="18" height="16"><rect x="2" y="1" width="10" height="10" fill="#9fd4e3" stroke="#3a93c2"/><rect x="13" y="11" width="4" height="4" fill="#9fd4e3" stroke="#3a93c2"/></svg>
    <svg width="22" height="16"><path d="M1 9l3 5 4-13h13" fill="none" stroke="#333"/><rect x="9" y="4" width="11" height="9" fill="#9fd4e3" stroke="#3a93c2"/></svg>
    <svg width="24" height="16"><path d="M3 9l3 5 4-13h13" fill="none" stroke="#333"/><rect x="11" y="4" width="11" height="9" fill="#9fd4e3" stroke="#3a93c2"/></svg>
    <svg width="20" height="18"><rect x="1" y="1" width="18" height="16" fill="#9fd4e3" stroke="#3a93c2"/></svg>
    <svg width="24" height="14"><rect x="4" y="3" width="7" height="8" fill="#9fd4e3" stroke="#3a93c2"/><rect x="13" y="3" width="7" height="8" fill="#9fd4e3" stroke="#3a93c2"/></svg>
    <span>f(x)</span><span>ln</span><span>log</span><span>log<sub>▫</sub></span><span>≥</span><span>≤</span><span>÷</span><span><i>π</i></span><span>∪</span><span>∩</span>
  </div>

  <div class="abs lbl" style="left:272px;top:755px">Enter Problem:</div>
  <div class="abs field" style="left:362px;top:749px;width:405px;height:52px"></div>

  <div class="abs lbl" style="left:272px;top:829px">Examples:</div>
  <div class="abs field examples" style="left:362px;top:823px;width:405px;height:109px">
    Algebra Concepts and Expressions<br>Points, Lines, and Line Segments<br>Simplifying Polynomials<br>Factoring Polynomials<br>Linear Equations
    <div class="abs scroll"></div>
  </div>

  <div class="abs lbl" style="left:275px;top:955px">Math Format:</div>
  <div class="abs btn" style="left:365px;top:950px;width:62px;height:22px;font-size:14px;line-height:20px">Show</div>

  <div class="abs lbl" style="left:274px;top:1004px">Math Format:</div>
  <div class="abs field" style="left:365px;top:1002px;width:405px;height:18px;border-radius:2px">
    <svg class="abs" style="right:3px;top:3px" width="11" height="11"><rect x="0.5" y="0.5" width="10" height="10" fill="#eee" stroke="#999"/><path d="M3 4h5l-2.5 3z" fill="#333"/></svg>
  </div>

  <div class="abs btn" style="left:363px;top:1051px;width:94px;height:26px;font-size:15px;line-height:24px">Answer</div>
</main>

<footer class="abs footer">
  <nav><a>Home</a>|<a>Algebra</a>|<a>Geometry</a>|<a>Trig</a>|<a>Calculus</a>|<a>Statistics</a>|<a>More</a>|<a>Subjects</a>|<a>Message Board</a></nav>
  <p>© Copyright 2006-2013 QuillNumberDesk.com</p>
</footer>
</body>
</html>
```